Business card and stationary for LOGISTICS company | ||
HAULVEX 514K | ||
Use same font as used in my logo | ||
Corporate Modern Professional Simple |
Oleksa | ||
Air and Sea freight from China to Ukraine | ||
Beijing, Lunmao Plaza C4-517K | ||
beijing@haulvex514k.com | ||
www.haulvex514k.com | ||
skype: mvoloshenko | ||
This business card would be given to the new registered client. After registration client receives his own client-number for air and for sea freight. I would need 2 lines on the back with plane and boat logo in front on it so I can write the clients number | ||

```html
<!DOCTYPE html>
<html lang="en">
<head>
<meta charset="utf-8">
<title>HAULVEX 514K Stationery</title>
<link href="https://fonts.googleapis.com/css2?family=Roboto:wght@400;700&display=swap" rel="stylesheet">
<style>
:root{
  --red:#e3141b;
  --blue:#1f57a6;
  --paper:#ffffff;
  --ink:#555555;
  --stage:#7a7a7a;
  --stage-dark:#4a4a4a;
}
*{box-sizing:border-box;margin:0;padding:0}
html,body{width:1200px;height:247px;overflow:hidden}
body{font-family:"Roboto",Arial,sans-serif;background:linear-gradient(180deg,#8a8a8a,var(--stage));position:relative}
.brand-panel{position:absolute;left:0;top:0;width:268px;height:150px;background:var(--stage-dark);display:flex;align-items:center;padding-left:24px;gap:10px}
.brand-dot{width:30px;height:30px;border-radius:50%;background:var(--red);flex:none}
.brand-name{color:var(--red);font-weight:700;font-size:24px;letter-spacing:.5px;white-space:nowrap}
.piece{position:absolute;background:var(--paper);overflow:hidden;box-shadow:1px 2px 4px rgba(0,0,0,.35)}
.piece svg.wave{position:absolute;left:0;bottom:0;width:100%}
.mark{display:flex;align-items:center;gap:3px;color:var(--red);font-weight:700;white-space:nowrap}
.mark i{display:block;border-radius:50%;background:var(--red);flex:none}
.tiny{font-size:3px;color:var(--ink);line-height:1.5}
.letter .mark{position:absolute;left:10px;top:10px;font-size:7px}
.letter .mark i{width:8px;height:8px}
.letter .body{position:absolute;left:12px;top:40px;right:12px}
.letter .sign{position:absolute;left:12px;bottom:58px;width:24px;height:1px;background:var(--ink)}
.card .mark{position:absolute;left:6px;top:6px;font-size:6px}
.card .mark i{width:6px;height:6px}
.card .tiny{position:absolute;right:6px;top:8px;text-align:right}
.card .tiny.left{left:6px;right:auto;top:6px;text-align:left}
.env .mark{position:absolute;left:8px;top:8px;font-size:7px}
.env .mark i{width:8px;height:8px}
.folder-cover{background:var(--red)}
.folder-cover .mark{position:absolute;left:8px;top:30px;font-size:8px;color:#fff}
.folder-cover .mark i{width:10px;height:10px;background:#fff}
</style>
</head>
<body>

<section class="brand-panel">
  <span class="brand-dot"></span>
  <span class="brand-name">HAULVEX 514K</span>
</section>

<!-- business cards -->
<div class="piece card" style="left:12px;top:160px;width:118px;height:38px">
  <div class="mark"><i></i>HAULVEX 514K</div>
  <svg class="wave" viewBox="0 0 100 20" preserveAspectRatio="none" height="14"><path d="M0 12 Q50 0 100 10 V20 H0Z" fill="var(--red)"/><path d="M0 10 Q50 -2 100 8" stroke="var(--blue)" stroke-width="1" fill="none"/></svg>
</div>
<div class="piece card" style="left:140px;top:160px;width:118px;height:38px">
  <div class="tiny left"><b>Oleksa</b><br>Lunmao Plaza C4-517K<br>beijing@haulvex514k.com<br>www.haulvex514k.com<br>skype: mvoloshenko</div>
  <svg class="wave" viewBox="0 0 100 20" preserveAspectRatio="none" height="10"><path d="M0 12 Q50 0 100 10 V20 H0Z" fill="var(--red)"/></svg>
</div>
<div class="piece card" style="left:12px;top:204px;width:118px;height:38px">
  <div class="mark"><i></i>HAULVEX 514K</div>
  <div class="tiny">Air freight no.<br>Sea freight no.</div>
  <svg class="wave" viewBox="0 0 100 20" preserveAspectRatio="none" height="10"><path d="M0 12 Q50 0 100 10 V20 H0Z" fill="var(--red)"/></svg>
</div>
<div class="piece card" style="left:140px;top:204px;width:118px;height:38px">
  <div class="mark"><i></i>HAULVEX 514K</div>
  <div class="tiny">Air and Sea freight<br>China to Ukraine</div>
  <svg class="wave" viewBox="0 0 100 20" preserveAspectRatio="none" height="10"><path d="M0 12 Q50 0 100 10 V20 H0Z" fill="var(--red)"/></svg>
</div>

<!-- letterheads -->
<div class="piece letter" style="left:288px;top:28px;width:130px;height:212px">
  <div class="mark"><i></i>HAULVEX 514K</div>
  <div class="body tiny">Dear client, thank you for choosing our air and sea freight service from China to Ukraine.</div>
  <div class="sign"></div>
  <svg class="wave" viewBox="0 0 100 40" preserveAspectRatio="none" height="48"><path d="M0 22 Q55 2 100 18 V40 H0Z" fill="var(--red)"/><path d="M0 18 Q55 -2 100 14" stroke="var(--blue)" stroke-width="1.2" fill="none"/></svg>
</div>
<div class="piece letter" style="left:428px;top:28px;width:130px;height:212px">
  <div class="mark"><i></i>HAULVEX 514K</div>
  <div class="body tiny">Beijing, Lunmao Plaza C4-517K<br>beijing@haulvex514k.com</div>
  <div class="sign"></div>
  <svg class="wave" viewBox="0 0 100 40" preserveAspectRatio="none" height="48"><path d="M0 22 Q55 2 100 18 V40 H0Z" fill="var(--red)"/><path d="M0 18 Q55 -2 100 14" stroke="var(--blue)" stroke-width="1.2" fill="none"/></svg>
</div>

<!-- compliment slip and small cards -->
<div class="piece card" style="left:572px;top:35px;width:132px;height:44px">
  <div class="mark"><i></i>HAULVEX 514K</div>
  <svg class="wave" viewBox="0 0 100 20" preserveAspectRatio="none" height="14"><path d="M0 12 Q50 0 100 10 V20 H0Z" fill="var(--red)"/><path d="M0 10 Q50 -2 100 8" stroke="var(--blue)" stroke-width="1" fill="none"/></svg>
</div>
<div class="piece card" style="left:572px;top:94px;width:72px;height:36px">
  <div class="mark"><i></i>HAULVEX 514K</div>
  <svg class="wave" viewBox="0 0 100 20" preserveAspectRatio="none" height="10"><path d="M0 12 Q50 0 100 10 V20 H0Z" fill="var(--red)"/></svg>
</div>
<div class="piece card" style="left:726px;top:35px;width:80px;height:46px">
  <div class="mark"><i></i>HAULVEX 514K</div>
  <svg class="wave" viewBox="0 0 100 20" preserveAspectRatio="none" height="12"><path d="M0 12 Q50 0 100 10 V20 H0Z" fill="var(--red)"/></svg>
</div>
<div class="piece card" style="left:726px;top:96px;width:64px;height:28px">
  <svg class="wave" viewBox="0 0 100 20" preserveAspectRatio="none" height="8"><path d="M0 12 Q50 0 100 10 V20 H0Z" fill="var(--red)"/></svg>
</div>

<!-- DL envelopes -->
<div class="piece env" style="left:572px;top:142px;width:138px;height:48px">
  <div class="mark"><i></i>HAULVEX 514K</div>
  <svg class="wave" viewBox="0 0 100 20" preserveAspectRatio="none" height="12"><path d="M0 12 Q50 0 100 10 V20 H0Z" fill="var(--red)"/><path d="M0 10 Q50 -2 100 8" stroke="var(--blue)" stroke-width="1" fill="none"/></svg>
</div>
<div class="piece env" style="left:572px;top:198px;width:138px;height:42px">
  <svg class="wave" viewBox="0 0 100 20" preserveAspectRatio="none" height="10"><path d="M0 12 Q50 0 100 10 V20 H0Z" fill="var(--red)"/></svg>
</div>

<!-- large envelopes -->
<div class="piece env" style="left:816px;top:78px;width:190px;height:60px;border:3px solid var(--blue)">
  <svg viewBox="0 0 190 60" width="184" height="54" style="position:absolute;left:0;top:0"><path d="M0 0 L92 30 L184 0" fill="none" stroke="#d8d8d8" stroke-width="1"/><rect x="0" y="44" width="184" height="10" fill="var(--red)"/></svg>
</div>
<div class="piece env" style="left:816px;top:148px;width:190px;height:86px">
  <div class="mark"><i></i>HAULVEX 514K</div>
  <svg class="wave" viewBox="0 0 100 20" preserveAspectRatio="none" height="18"><path d="M0 12 Q50 0 100 10 V20 H0Z" fill="var(--red)"/><path d="M0 10 Q50 -2 100 8" stroke="var(--blue)" stroke-width="1" fill="none"/></svg>
</div>

<!-- presentation folder -->
<div class="piece folder-cover" style="left:1012px;top:28px;width:92px;height:212px">
  <div class="mark"><i></i>HAULVEX 514K</div>
</div>
<div class="piece" style="left:1104px;top:28px;width:92px;height:212px">
  <svg class="wave" viewBox="0 0 100 100" preserveAspectRatio="none" height="150"><path d="M0 30 Q50 0 100 22 V100 H0Z" fill="var(--red)"/><path d="M0 26 Q50 -4 100 18" stroke="var(--blue)" stroke-width="1" fill="none"/></svg>
</div>

</body>
</html>
```